Inspirational Card with Words of Wisdom to Give to Kids

I run basketball camps and give inspirational messages to elementary schools and high schools (www.pastthebrightline.net).

I would like to create a card that has some inspirational thoughts and words of wisdom on it that I can give away...and that students and athletes will keep in their wallet as a reminder of things I've taught them.

I want it to be clean and classy, while not looking too child-like or business-like, as I'd like to be able to give it out to kids, teenagers, and young adults.

The card will be the size of a regular business card and will be double-sided. I would like to use black, orange, gray, and white as the primary colors, with white or gray likely being the background color.
Updates

You're welcome to leave off the title "Wisdom for Life" if desired and just use "The Triple Crown of Success" on the front of the card.

Thanks.

If you choose to leave off the poem, which you're welcome to do, please make one minor addition to the 5-point creed:

Add the words "God and" to "Honour others in everything you say and do" so it becomes:

"Honour God and others in everything you say and do."

Target Market(s)

Children, Teenagers, and Young Adults

Industry/Entity Type

Business

Requirements
Must have
• All the content, although the poem could be removed if necessary.
Should not have
• Nothing basketball-specific, as I want to be able to give it out to any child or teenager.

```html
<!DOCTYPE html>
<html lang="en">
<head>
<meta charset="utf-8">
<title>The Triple Crown of Success – Pocket Card</title>
<link href="https://fonts.googleapis.com/css2?family=Lexend:wght@500;700;800&family=Mulish:ital,wght@0,400;0,600;0,700;0,800;1,400&display=swap" rel="stylesheet">
<style>
  :root {
    --orange: #dd6b1e;
    --orange-light: #ec8a43;
    --black: #141414;
    --white: #ffffff;
    --gray: #e2e2e2;
    --gray-line: #bdbdbd;
    --backdrop: #ebe8e4;
    --ink: #1a1a1a;
  }
  * { box-sizing: border-box; margin: 0; padding: 0; }
  html, body { width: 1200px; height: 880px; overflow: hidden; }
  body {
    background: var(--backdrop);
    position: relative;
    font-family: "Mulish", Arial, sans-serif;
    color: var(--ink);
  }
  .card {
    position: absolute;
    width: 720px;
    height: 411px;
    overflow: hidden;
    background: var(--orange);
    box-shadow: 0 6px 18px rgba(0,0,0,.18);
  }
  .card--front { left: 440px; top: 20px; }
  .card--back { left: 40px; top: 449px; background: var(--white); }
  .card__shapes { position: absolute; inset: 0; }

  /* ---------- front ---------- */
  .mosaic {
    position: absolute;
    right: 0; top: 180px;
    width: 300px; height: 231px;
    background: radial-gradient(ellipse at 70% 60%, var(--orange-light) 0%, rgba(236,138,67,0) 70%);
  }
  .title {
    position: absolute;
    left: 95px; top: 20px;
    font-family: "Lexend", Arial, sans-serif;
    font-weight: 800;
    line-height: 1;
    text-transform: uppercase;
  }
  .title__the { display: block; font-size: 21px; color: var(--black); }
  .title__main { display: block; font-size: 44px; color: var(--black); letter-spacing: -0.5px; margin-top: 2px; }
  .title__sub { display: block; font-size: 35px; color: var(--orange); margin: 2px 0 0 112px; }

  .rule-col { position: absolute; }
  .rule-col--never { left: 40px; top: 136px; }
  .rule-col--dont { left: 248px; top: 152px; }
  .rule-col--always { left: 456px; top: 167px; }
  .pill {
    display: inline-block;
    background: linear-gradient(var(--black) 0 50%, #2c2c2c 50% 100%);
    color: var(--white);
    font-family: "Lexend", Arial, sans-serif;
    font-weight: 700;
    font-size: 25px;
    letter-spacing: 1px;
    line-height: 36px;
    height: 36px;
    padding: 0 26px;
    border-radius: 18px;
  }
  .rule-list {
    list-style: none;
    margin: 6px 0 0 6px;
    color: var(--white);
    font-size: 20px;
    font-weight: 600;
    line-height: 26px;
  }
  .rule-list li::before { content: "•"; margin-right: 8px; }
  .rule-list .wrap { padding-left: 20px; }
  .rule-list .wrap::before { content: none; }

  .quote {
    position: absolute;
    left: 150px; top: 330px;
    width: 520px;
    text-align: center;
    color: var(--white);
    font-weight: 800;
    font-size: 21px;
    line-height: 26px;
  }
  .credit {
    position: absolute;
    right: 40px; top: 377px;
    text-align: right;
    color: var(--black);
    font-size: 12px;
    line-height: 14px;
    white-space: nowrap;
  }
  .credit__name { margin-right: 20px; }

  /* ---------- back ---------- */
  .creed-tag {
    position: absolute;
    left: 92px; top: 20px;
    background: var(--black);
    color: var(--white);
    font-family: "Lexend", Arial, sans-serif;
    font-weight: 700;
    font-size: 21px;
    letter-spacing: .5px;
    line-height: 32px;
    padding: 0 20px;
    border-radius: 16px;
  }
  .creed {
    position: absolute;
    left: 42px; top: 62px;
    list-style: none;
    font-size: 20px;
    line-height: 27px;
    counter-reset: creed;
  }
  .creed li { counter-increment: creed; white-space: nowrap; }
  .creed li::before { content: counter(creed) ". "; color: var(--orange); }

  .pledge {
    position: absolute;
    left: 0; top: 212px;
    width: 720px; height: 148px;
    background: var(--orange);
  }
  .pledge__text {
    margin: 8px auto 0;
    width: 640px;
    text-align: center;
    font-size: 20px;
    line-height: 25px;
    color: var(--black);
  }
  .pledge__text strong { font-weight: 800; }
  .sign-field { position: absolute; top: 84px; width: 232px; }
  .sign-field--name { left: 44px; }
  .sign-field--date { left: 396px; }
  .sign-field__box {
    height: 34px;
    background: var(--gray);
    border: 1px solid var(--gray-line);
  }
  .sign-field__label {
    text-align: center;
    font-family: "Lexend", Arial, sans-serif;
    font-size: 9px;
    font-weight: 700;
    letter-spacing: .5px;
    margin-top: 3px;
    color: var(--black);
  }
  .values {
    position: absolute;
    left: 0; bottom: 0;
    width: 720px; height: 51px;
    background: var(--black);
    color: var(--white);
    font-size: 16px;
    line-height: 51px;
    text-align: center;
  }
  .values strong { font-weight: 800; }
</style>
</head>
<body>

<section class="card card--front" aria-label="Card front">
  <div class="mosaic" role="img" aria-label="Faint square mosaic pattern in lighter orange"></div>
  <svg class="card__shapes" width="720" height="411" viewBox="0 0 720 411" aria-hidden="true">
    <polygon points="0,0 720,0 720,168 0,118" fill="var(--white)"/>
    <polygon points="0,118 720,168 720,176 0,126" fill="var(--black)"/>
    <polygon points="0,318 720,338 720,374 0,354" fill="var(--black)"/>
  </svg>

  <h1 class="title">
    <span class="title__the">The</span>
    <span class="title__main">Triple Crown</span>
    <span class="title__sub">of Success</span>
  </h1>

  <div class="rule-col rule-col--never">
    <span class="pill">NEVER</span>
    <ul class="rule-list"><li>Lie</li><li>Cheat</li><li>Steal</li></ul>
  </div>
  <div class="rule-col rule-col--dont">
    <span class="pill">DON'T</span>
    <ul class="rule-list"><li>Blame</li><li>Complain</li><li>Give Up</li></ul>
  </div>
  <div class="rule-col rule-col--always">
    <span class="pill">ALWAYS</span>
    <ul class="rule-list"><li>Be Grateful</li><li>Uplift Others</li><li>Do More Than</li><li class="wrap">Your Share</li></ul>
  </div>

  <p class="quote">“Make each day your masterpiece.”</p>
  <p class="credit"><span class="credit__name">- Coach Jonah Whitfield</span><br>(The source of inspiration for this card)</p>
</section>

<section class="card card--back" aria-label="Card back">
  <h2 class="creed-tag">A 5-POINT CREED</h2>
  <ol class="creed">
    <li>Honor God and others in everything you say and do.</li>
    <li>Act with integrity and uprightness in all matters.</li>
    <li>Be intentional to grow and learn new things each day.</li>
    <li>Prioritize serving and giving to others above yourself.</li>
    <li>Dream, pray for, and expect the impossible.</li>
  </ol>

  <div class="pledge">
    <p class="pledge__text">I commit to doing my best to live out the<br><strong>TRIPLE CROWN</strong> and <strong>5-POINT CREED</strong> each day.</p>
    <div class="sign-field sign-field--name"><div class="sign-field__box"></div><p class="sign-field__label">SIGNATURE</p></div>
    <div class="sign-field sign-field--date"><div class="sign-field__box"></div><p class="sign-field__label">DATE</p></div>
  </div>

  <p class="values"><strong>Live every day with:</strong> Passion • Wonder • Playfulness • Gratitude • Love</p>
</section>

</body>
</html>
```